elec business card

hi all

Im after a new age looking business card with my company logo on it

must include these details, I would like the PH and Email to be symbols

If the colours used for card could be kept within the colours used in logo that I have supplied that would be great, if another colour is to be used dark grey would be ok. no light bulbs etc thanks

Details below to be incorporated on card

Dorian Pellow

Lic E781392

PH 0219467318

E info@brightwayelectrical.example.nz

Domestic Commercial Industrial Electricians

```html
<!DOCTYPE html>
<html lang="en">
<head>
<meta charset="utf-8">
<title>Brightway Electrical – Business Card</title>
<link href="https://fonts.googleapis.com/css2?family=Montserrat:wght@400;500;700&display=swap" rel="stylesheet">
<style>
  :root {
    --backdrop: #d9d8d5;
    --card-white: #ffffff;
    --card-dark: #2a2b2e;
    --brand-blue: #0f72c4;
    --ink: #222326;
    --ink-soft: #4a4b4f;
    --paper-white: #ffffff;
  }
  * { box-sizing: border-box; margin: 0; padding: 0; }
  html, body {
    width: 1200px; height: 801px; overflow: hidden;
    background: var(--backdrop);
    font-family: "Montserrat", sans-serif;
  }
  .canvas {
    position: relative; width: 1200px; height: 801px;
    display: flex; align-items: center; justify-content: center; gap: 40px;
  }
  .card {
    position: relative; width: 540px; height: 309px;
    box-shadow: 0 6px 18px rgba(0,0,0,.18);
    overflow: hidden;
  }
  .card--front { background: var(--card-white); color: var(--ink); }
  .card--back { background: var(--card-dark); color: var(--paper-white); }

  /* brand name block */
  .brand {
    display: flex; align-items: center; gap: 12px;
    color: var(--brand-blue); font-weight: 700;
    text-transform: uppercase; line-height: 1.05;
  }
  .brand__dot {
    flex: none; border-radius: 50%; background: var(--brand-blue);
  }
  .brand__name { display: flex; flex-direction: column; }

  .card--front .brand {
    position: absolute; top: 42px; right: 40px;
    font-size: 26px; letter-spacing: 1px;
  }
  .card--front .brand__dot { width: 34px; height: 34px; }

  .divider {
    position: absolute; left: 214px; right: 36px; top: 150px;
    height: 1.5px; background: var(--ink);
  }
  .person { position: absolute; left: 36px; top: 136px; }
  .person__name {
    color: var(--brand-blue); font-weight: 700; font-size: 19px;
    letter-spacing: .3px; text-transform: uppercase;
  }
  .person__role { font-weight: 500; font-size: 14px; margin-top: 3px; }

  .contact {
    position: absolute; left: 36px; top: 202px;
    list-style: none; font-size: 13.5px; color: var(--ink-soft);
    display: flex; flex-direction: column; gap: 6px;
  }
  .contact__item { display: flex; align-items: center; gap: 8px; }
  .contact__icon { width: 14px; height: 14px; flex: none; }

  .card--back .brand {
    position: absolute; left: 0; right: 0; top: 92px;
    justify-content: center; font-size: 36px; letter-spacing: 2px;
  }
  .card--back .brand__dot { width: 48px; height: 48px; }
  .tagline {
    position: absolute; left: 0; right: 0; bottom: 58px;
    text-align: center; font-size: 14px; font-weight: 500; letter-spacing: .8px;
  }
</style>
</head>
<body>
<main class="canvas">
  <section class="card card--front" aria-label="Card front">
    <div class="brand">
      <span class="brand__dot"></span>
      <span class="brand__name"><span>Brightway</span><span>Electrical</span></span>
    </div>
    <div class="divider"></div>
    <div class="person">
      <p class="person__name">Dorian Pellow</p>
      <p class="person__role">Director</p>
    </div>
    <ul class="contact">
      <li class="contact__item">Lic E781392</li>
      <li class="contact__item">
        <svg class="contact__icon" viewBox="0 0 24 24" aria-label="Phone"><path fill="var(--brand-blue)" d="M6.6 10.8a15 15 0 0 0 6.6 6.6l2.2-2.2a1 1 0 0 1 1-.25 11.4 11.4 0 0 0 3.6.57 1 1 0 0 1 1 1V20a1 1 0 0 1-1 1A17 17 0 0 1 3 4a1 1 0 0 1 1-1h3.5a1 1 0 0 1 1 1c0 1.25.2 2.45.57 3.57a1 1 0 0 1-.25 1z"/></svg>
        0219467318
      </li>
      <li class="contact__item">
        <svg class="contact__icon" viewBox="0 0 24 24" aria-label="Email"><rect x="2" y="5" width="20" height="14" rx="1.5" fill="var(--brand-blue)"/><path d="M3 6l9 7 9-7" fill="none" stroke="#fff" stroke-width="1.6"/></svg>
        info@brightwayelectrical.example.nz
      </li>
    </ul>
  </section>

  <section class="card card--back" aria-label="Card back">
    <div class="brand">
      <span class="brand__dot"></span>
      <span class="brand__name"><span>Brightway</span><span>Electrical</span></span>
    </div>
    <p class="tagline">Domestic Commercial Industrial Electricians</p>
  </section>
</main>
</body>
</html>
```